Private School Website Revamp

We need a new design for the private school's website revamp. The new website will be using WordPress CMS, but we will be using it to handle custom data types, not blogs - so the content will not be typical blog-style.

The school has indicated the following template which they like, and our design to follow the design style.
http://mvr7.layout-demoes.com/sitetheme_48172/
However, follow the school's colour-theme and sitemap.

Colour-theme: White, Green (refer to current website - www.ruolinvo.com.sg)

Sitemap: (for navigation menu)
- Home
- Academic & Examination Board
- Our Philosophy
- Our Programmes
+ Preparatory Courses
+ Tuition Classes
+ Study Tours
- Our Hostel
- Trial Tests
+ English
+ Mathematics
- Contact Us

Target Market(s)

Parents looking for private school services.
Existing students of the private school accessing trial tests.

Industry/Entity Type

School

Requirements
Must have
• Homepage design to include
• - Logo, navigation menu, search box
• - Featured area/slideshow (see prefered template above)
• - Section for Preparatory Courses
• - Section for Tuition Classes
• - Section for Study Tours
• - Section for Hostel Stay
• - Awards & Certification box
• - Footer contact details
Nice to have
• - Pictures of happy students
• - The Message from Director box is "nice to have", but no necessary if it does not fit into homepage design.

```html
<!DOCTYPE html>
<html lang="en">
<head>
<meta charset="utf-8">
<title>Ruolinvo Private School</title>
<link rel="stylesheet" href="https://fonts.googleapis.com/css2?family=PT+Serif:wght@400;700&family=Open+Sans:wght@400;600;700&family=Arimo&display=swap">
<style>
:root{
  --green-dark:#1f4a0c;
  --green:#5a9e1e;
  --green-light:#8cc63f;
  --lime:#b7df4a;
  --yellow:#f9cf1c;
  --orange:#f2a31f;
  --cyan:#29d4de;
  --sky:#2fc6ec;
  --text:#222;
  --line:#bbb;
}
*{margin:0;padding:0;box-sizing:border-box}
html,body{width:756px;height:1200px;overflow:hidden}
body{position:relative;background:linear-gradient(#b9d8e3 0,#e6f0f1 110px,#fff 140px);font-family:"Arimo",sans-serif;color:var(--text)}
.abs{position:absolute}
.brand{left:23px;top:26px;color:var(--green-dark);font-family:"PT Serif",serif}
.brand-mark{font-size:28px;letter-spacing:4px;line-height:38px}
.brand-name{font-size:14.5px;line-height:18px;margin-top:6px}
.toplinks{right:35px;top:45px;font-family:"PT Serif",serif;font-size:11.5px;color:var(--green-dark)}
.toplinks span{margin:0 8px}
.search{right:35px;top:70px;display:flex;align-items:center;gap:4px}
.search-input{width:130px;height:18px;border:1px solid #8aa;background:#fff;font-family:"Open Sans",sans-serif;font-size:8.5px;color:#888;line-height:16px;padding-left:5px}
.search-btn{width:22px;height:18px;border-radius:3px;background:linear-gradient(#92d04a,#5a9e1e);display:flex;align-items:center;justify-content:center}
.nav{left:17px;top:110px;display:flex;gap:3px}
.tab{height:23px;padding:0 11px;border-radius:4px 4px 0 0;font-family:"PT Serif",serif;font-size:11px;line-height:23px;color:#222;background:linear-gradient(#ffe766,var(--yellow));white-space:nowrap}
.tab.active{background:linear-gradient(#92d04a,#6db52c);color:#fff}
.navline{left:8px;top:132px;width:740px;height:4px;background:var(--green-light)}
.page{left:8px;top:136px;width:740px;height:1042px;border:1px solid #ccc;border-top:none;background:#fff}
.hero{left:19px;top:149px;width:717px;height:248px;border-radius:8px;background:linear-gradient(100deg,#c9a27a 0%,#6f6a57 35%,#8e8a6b 55%,#6f5a3e 80%,#4a3b2a 100%)}
.hero-text{right:24px;top:340px;text-align:right;font-family:"PT Serif",serif;font-weight:700;font-size:24px;line-height:27px;color:#fff;text-shadow:1px 1px 2px #000}
.box{border:1px solid #e2e2e2;border-radius:8px;background:linear-gradient(#fff,#f6f7fa)}
.box h2{font-family:"PT Serif",serif;font-weight:400;font-size:19px;color:var(--green-dark);margin:10px 9px 0;padding-bottom:7px;border-bottom:1px dotted var(--line)}
.box p{font-size:8.9px;line-height:13.6px;margin:12px 9px 0;color:#222}
.box h3{font-family:"PT Serif",serif;font-weight:400;font-size:15px;color:var(--green-dark);padding-bottom:5px;border-bottom:1px dotted var(--line)}
.programmes{left:9px;top:160px;width:519px}
.cards{display:flex;gap:9px;margin-top:9px}
.card{width:123px}
.card-photo{height:58px;border-radius:5px}
.card h4{font-family:"PT Serif",serif;font-weight:700;font-size:10.5px;color:var(--green-dark);margin-top:6px}
.card .txt{font-size:8.4px;line-height:12px;margin-top:3px}
.card .link{font-family:"Open Sans",sans-serif;font-weight:700;font-size:7.8px;color:var(--green);margin-top:4px}
.awards{left:9px;top:330px;width:519px}
.badges{display:flex;gap:14px;margin-top:11px;align-items:center}
.badge{width:54px;height:44px;border-radius:5px;background:linear-gradient(#eef6e2,#cfe6b0);border:1px solid #b7d48f}
.badge.round{width:44px;border-radius:50%}
.side{border-radius:8px;padding:3px}
.side .head{height:23px;border-radius:6px;font-family:"PT Serif",serif;font-size:13.5px;line-height:23px;text-align:center;color:#fff;text-shadow:0 1px 1px rgba(0,0,0,.3)}
.item{margin:6px 10px 0;padding-bottom:7px;border-bottom:1px dotted #6a8a6a;font-family:"Open Sans",sans-serif;font-size:7.6px}
.item a{color:#111;text-decoration:underline;display:block;line-height:12px}
.item .by{text-align:right;font-weight:700;margin-top:3px}
.more{margin:10px 10px 0;display:flex;align-items:center;gap:5px;font-family:"Open Sans",sans-serif;font-weight:700;font-size:8px;color:#1f3a10}
.parents{background:linear-gradient(#e8fbfb,var(--cyan))}
.parents .head{background:linear-gradient(#5ee5ea,#12b9c4)}
.students{background:linear-gradient(#f3f9e6,var(--lime))}
.students .head{background:linear-gradient(#9bd84a,#62b322)}
.agent{background:linear-gradient(#fffbe8,#f8d24a)}
.agent .head{background:linear-gradient(#f8c050,var(--orange))}
.contact{background:linear-gradient(#eafbff,var(--sky))}
.contact .head{background:linear-gradient(#5fd8f5,#18b3e0)}
.field{font-family:"Open Sans",sans-serif;font-weight:700;font-size:8px;color:#222}
.input{width:96px;height:15px;border:1px solid #777;background:#fff}
.submit{width:53px;height:14px;background:linear-gradient(#ffd766,#f6a912);border:1px solid #c98000;font-family:"Open Sans",sans-serif;font-weight:700;font-size:8px;text-align:center;line-height:12px}
.c-label{font-family:"PT Serif",serif;font-size:10.5px;color:#111}
.c-num{font-family:"Open Sans",sans-serif;font-weight:700;font-size:15.5px;color:#111;line-height:20px}
.footline{left:16px;top:1037px;width:723px;height:4px;background:var(--green)}
.footer{left:16px;top:1044px;width:723px;height:124px;background:linear-gradient(#2f6e0c,#7bbf2e)}
.addr{left:26px;top:1054px;color:#fff;font-family:"Open Sans",sans-serif;font-weight:700;font-size:8px;line-height:13.6px}
.addr h3{font-family:"PT Serif",serif;font-weight:400;font-size:14px;color:#1a3a05;line-height:18px;margin-bottom:2px}
.foot-brand{right:38px;top:1056px;text-align:right;color:#fff;font-family:"PT Serif",serif}
.foot-brand .m{font-size:24px;letter-spacing:4px;line-height:34px}
.foot-brand .n{font-size:14px;margin-top:5px}
.copy{right:40px;top:1125px;color:#fff;font-family:"Open Sans",sans-serif;font-weight:700;font-size:8px}
</style>
</head>
<body>
<div class="abs brand"><div class="brand-mark">Ruolinvo</div><div class="brand-name">RUOLINVO PRIVATE SCHOOL</div></div>
<div class="abs toplinks">About Us<span>|</span>Contact Us</div>
<div class="abs search">
  <div class="search-input">Search...</div>
  <div class="search-btn"><svg width="11" height="11" viewBox="0 0 11 11"><circle cx="4.5" cy="4.5" r="3.3" stroke="#fff" stroke-width="1.4" fill="none"/><path d="M7 7l3 3" stroke="#fff" stroke-width="1.6"/></svg></div>
</div>

<nav class="abs nav">
  <div class="tab active">Home</div>
  <div class="tab">Academic &amp; Examination Board</div>
  <div class="tab">Our Philosophy</div>
  <div class="tab">Our Programmes</div>
  <div class="tab">Our Hostel</div>
  <div class="tab">Trial Tests</div>
  <div class="tab">Contact Us</div>
</nav>
<div class="abs navline"></div>
<div class="abs page"></div>

<div class="abs hero" role="img" aria-label="Photo of smiling pupils and children working on laptops in a classroom"></div>
<div class="abs hero-text">Securing Best Education<br>For Your Child</div>

<section class="abs box" style="left:17px;top:410px;width:539px;height:176px">
<h2>WHY US?</h2>
<p>Ut ut urna libero, eget malesuada ante. Aliquam eu lectus id dolor hendrerit accumsan id nec nulla. Suspendisse potenti. Etiam in nisi nibh, ut pulvinar mi. Aliquam sodales congue urna, in dapibus ligula laoreet non. Suspendisse gravida, lorem id mollis tristique,</p>
<p>Sed posuere posuere arcu, in venenatis purus fringilla vel. Etiam bibendum tempus nisl, eget condimentum nibh suscipit a. Nulla elementum, orci in fermentum consequat, est tellus ullamcorper augue, sed posuere tellus tortor ac erat. Sed egestas condimentum ipsum in tristique. In id quam et nibh fringilla ornare.</p>
</section>

<section class="abs box" style="left:17px;top:599px;width:539px;height:426px">
<h2>HOW TO APPLY?</h2>
<p>Ut ut urna libero, eget malesuada ante. Aliquam eu lectus id dolor hendrerit accumsan id nec nulla. Suspendisse potenti. Etiam in nisi nibh, ut pulvinar mi. Aliquam sodales congue urna, in dapibus ligula laoreet non. Suspendisse gravida, lorem id mollis tristique,</p>
<p>Sed posuere posuere arcu, in venenatis purus fringilla vel. Etiam bibendum tempus nisl, eget condimentum nibh suscipit a. Nulla elementum, orci in fermentum consequat, est tellus ullamcorper augue, sed posuere tellus tortor ac erat. Sed egestas condimentum ipsum in tristique. In id quam et nibh fringilla ornare.</p>

<div class="abs programmes">
  <h3>Our Programmes</h3>
  <div class="cards">
    <div class="card">
      <div class="card-photo" role="img" aria-label="Photo of a preparatory class" style="background:linear-gradient(120deg,#a9c98a,#5e8f3a)"></div>
      <h4>Preparatory Courses</h4>
      <div class="txt">Full-time courses helping foreign students enter local schools.</div>
      <div class="link">Read More »</div>
    </div>
    <div class="card">
      <div class="card-photo" role="img" aria-label="Photo of a tuition lesson" style="background:linear-gradient(120deg,#f6e29a,#d9a83a)"></div>
      <h4>Tuition Classes</h4>
      <div class="txt">Small-group lessons for local students in core subjects.</div>
      <div class="link">Read More »</div>
    </div>
    <div class="card">
      <div class="card-photo" role="img" aria-label="Photo of students on a study tour" style="background:linear-gradient(120deg,#a9e2ef,#3fa6c6)"></div>
      <h4>Study Tours</h4>
      <div class="txt">Short visits that mix classroom study with city learning.</div>
      <div class="link">Read More »</div>
    </div>
    <div class="card">
      <div class="card-photo" role="img" aria-label="Photo of the hostel rooms" style="background:linear-gradient(120deg,#e7cfae,#a57b52)"></div>
      <h4>Hostel Stay</h4>
      <div class="txt">Safe, supervised rooms close to the school campus.</div>
      <div class="link">Read More »</div>
    </div>
  </div>
</div>

<div class="abs awards">
  <h3>Awards &amp; Certification</h3>
  <div class="badges">
    <div class="badge round"></div>
    <div class="badge"></div>
    <div class="badge round"></div>
    <div class="badge"></div>
    <div class="badge round"></div>
  </div>
</div>
</section>

<aside class="abs side parents" style="left:568px;top:412px;width:171px;height:174px">
<div class="head">Parents Testimonials</div>
<div class="item"><a>Nuno valencia esta de demaria valen andn uno di cartia margarute .</a><div class="by">Mr. Kwee, 16-04-2010</div></div>
<div class="item"><a>Nuno valencia esta de demaria valen andn uno di cartia margarute .</a><div class="by">Mrs. Lena Tan, 11-06-2010</div></div>
<div class="more"><svg width="18" height="18" viewBox="0 0 18 18"><circle cx="9" cy="9" r="8" fill="#6d7b86" stroke="#dfe6ea"/><path d="M6 5l4 4-4 4M9 5l4 4-4 4" stroke="#fff" stroke-width="1.4" fill="none"/></svg>Read More Testimonials</div>
</aside>

<aside class="abs side students" style="left:568px;top:601px;width:171px;height:176px">
<div class="head">Students Testimonials</div>
<div class="item"><a>Nuno valencia esta de demaria  valen andn uno di cartia margarute .</a><div class="by">Mr. B. Ortan, 16-04-2010</div></div>
<div class="item"><a>Lorem ipsum dolor sit amet di val end andn uno di cartia margarute .</a><div class="by">Mrs. Lena Tan, 11-06-2010</div></div>
<div class="more"><svg width="18" height="18" viewBox="0 0 18 18"><circle cx="9" cy="9" r="8" fill="#6d7b86" stroke="#dfe6ea"/><path d="M6 5l4 4-4 4M9 5l4 4-4 4" stroke="#fff" stroke-width="1.4" fill="none"/></svg>Read More Testimonials</div>
</aside>

<aside class="abs side agent" style="left:568px;top:792px;width:171px;height:109px">
<div class="head">Agent Login</div>
<div class="abs field" style="left:29px;top:38px">Login</div>
<div class="abs input" style="left:64px;top:35px"></div>
<div class="abs field" style="left:10px;top:60px">Password</div>
<div class="abs input" style="left:64px;top:58px"></div>
<div class="abs submit" style="left:64px;top:81px">Submit</div>
</aside>

<aside class="abs side contact" style="left:568px;top:916px;width:171px;height:109px">
<div class="head">Contact Us</div>
<div style="margin:10px 0 0 11px">
<div class="c-label">Telephone No.</div>
<div class="c-num">+65 6123 4870</div>
<div class="c-label" style="margin-top:3px">Fax:</div>
<div class="c-num">+65 6123 4871</div>
</div>
</aside>

<div class="abs footline"></div>
<footer class="abs footer"></footer>
<div class="abs addr">
<h3>Address</h3>
48 Maple Grove Rd 17<br>
Linden Park Community Hall, # 02 -05<br>
S(604512)<br>
Telephone No. +65 6123 4870<br>
Fax: +65 6123 4871<br>
Email: office@ruolinvo.com.sg
</div>
<div class="abs foot-brand"><div class="m">Ruolinvo</div><div class="n">RUOLINVO PRIVATE SCHOOL</div></div>
<div class="abs copy">© 2010, Ruolinvo Private School &nbsp;&nbsp;|&nbsp;&nbsp; All Rghts Reserved</div>
</body>
</html>
```